Diverse, up-scale salon needs eye-catching, unique business cards.

We are looking for a unique business card design for our stylist but that can also be multi functional and used for appointment reminder and referrals. I will need a design in a format that I can modify names and titles going forward. In the past we have had a dark background with the logo on one side, and stylist and contact information on the other but we are open to all ideas. I have included our mission statement as well as branded colors below. The statement doesn't need to go on the card, it's just a reference for target market. We need space for the stylists name, title, instagram handle and then the salons phone number, website and address. I am also open to adding a spot for a qr code linked to the stylist instagram or the salon booking link.

primary brand colors:
#333333 #233415 #36502a #93874a #000000
Mission statement:
Morvane Hair Studio, a high-end salon located in the lively Downtown Farmington, Michigan, is committed to providing exceptional services in a welcoming and relaxed environment to meet the needs of our diverse clientele.
Our salon specializes in contemporary custom haircuts, coloring, extensions, and barbering and beard grooming services. Our team of skilled stylists is passionate and inventive in their hair styling techniques. At the heart of our salon are values centered on quality, innovation, creativity, and above all, comfort. These core values are evident in every appointment across our customizable array of services.
Our goal is to establish a benchmark for exceptional hair care for every human.
Website: www.morvanehairstudio-demo.com
instagram: @morvanehairstudio
address: 41872 Pelton Brook Rd, Larkfield MI
phone: 555-316-8847

Industry/Entity Type

Hair Salon

Contact Information for Business Card

Stylist name, title, phone, instagram, website, address, (optional qr code)

Requirements
Should not have
• Does not need mission statement on the card.

```html
<!DOCTYPE html>
<html lang="en">
<head>
<meta charset="utf-8">
<title>Morvane Hair Studio – Business Card</title>
<link href="https://fonts.googleapis.com/css2?family=Cinzel:wght@500&family=Montserrat:wght@400;500&display=swap" rel="stylesheet">
<style>
  :root {
    --backdrop: #333333;
    --card: #141414;
    --card-back: #111111;
    --pattern-tone: #1c1c1c;
    --gold: #93874a;
    --ink-light: #f2f2f2;
  }
  html, body {
    margin: 0;
    width: 1200px;
    height: 801px;
    overflow: hidden;
    background: var(--backdrop);
  }
  .stage {
    position: relative;
    width: 1200px;
    height: 801px;
  }
  .card {
    position: absolute;
    top: 246px;
    width: 540px;
    height: 309px;
    box-sizing: border-box;
    border: 2px solid var(--gold);
    box-shadow: 0 10px 30px rgba(0,0,0,0.45);
    overflow: hidden;
  }
  .card-front { left: 40px; background: var(--card); }
  .card-back  { left: 620px; background: var(--card-back); }

  /* front: brand block */
  .brand-block {
    position: absolute;
    left: 28px;
    top: 0;
    width: 190px;
    height: 305px;
    display: flex;
    flex-direction: column;
    align-items: center;
    justify-content: center;
    gap: 14px;
  }
  .brand-dot {
    width: 14px;
    height: 14px;
    border-radius: 50%;
    background: var(--gold);
  }
  .brand-name {
    font-family: "Montserrat", sans-serif;
    font-weight: 500;
    color: var(--gold);
    font-size: 17px;
    letter-spacing: 3px;
    text-transform: uppercase;
    line-height: 1.5;
    text-align: center;
    margin: 0;
  }
  .divider {
    position: absolute;
    left: 238px;
    top: 40px;
    width: 1.5px;
    height: 225px;
    background: var(--gold);
  }

  /* front: contact block */
  .contact {
    position: absolute;
    left: 262px;
    top: 44px;
    right: 14px;
    font-family: "Montserrat", sans-serif;
    color: var(--ink-light);
    font-size: 14px;
    line-height: 1.3;
  }
  .stylist-name {
    font-family: "Cinzel", serif;
    font-weight: 500;
    color: var(--gold);
    font-size: 25px;
    letter-spacing: 1px;
    margin: 0;
  }
  .stylist-title { margin: 0 0 18px; }
  .address { margin: 0 0 18px; }
  .contact-list { list-style: none; margin: 0; padding: 0; }
  .contact-list li {
    display: flex;
    align-items: center;
    gap: 8px;
    margin-bottom: 4px;
    font-size: 13px;
    white-space: nowrap;
  }
  .contact-icon { width: 12px; height: 12px; flex: none; }

  /* back */
  .monogram-pattern {
    position: absolute;
    inset: 0;
    background: linear-gradient(120deg, #0c0c0c 0%, var(--pattern-tone) 55%, #2a2a2a 100%);
  }
  .back-name {
    position: absolute;
    right: 42px;
    top: 140px;
    font-family: "Montserrat", sans-serif;
    font-weight: 500;
    color: var(--gold);
    font-size: 13px;
    letter-spacing: 1.5px;
    text-transform: uppercase;
    margin: 0;
  }
</style>
</head>
<body>
<main class="stage">

  <section class="card card-front">
    <div class="brand-block">
      <span class="brand-dot" aria-hidden="true"></span>
      <p class="brand-name">Morvane<br>Hair Studio</p>
    </div>
    <div class="divider"></div>
    <div class="contact">
      <h1 class="stylist-name">MARISOL</h1>
      <p class="stylist-title">President</p>
      <p class="address">41872 Pelton Brook Rd<br>Larkfield MI</p>
      <ul class="contact-list">
        <li>
          <svg class="contact-icon" viewBox="0 0 24 24" aria-hidden="true"><path fill="#93874a" d="M6.6 10.8a15 15 0 0 0 6.6 6.6l2.2-2.2c.3-.3.7-.4 1-.2 1.1.4 2.3.6 3.6.6.6 0 1 .4 1 1V20c0 .6-.4 1-1 1A17 17 0 0 1 3 4c0-.6.4-1 1-1h3.5c.6 0 1 .4 1 1 0 1.3.2 2.5.6 3.6.1.3 0 .7-.2 1z"/></svg>
          <span>555-316-8847</span>
        </li>
        <li>
          <svg class="contact-icon" viewBox="0 0 24 24" aria-hidden="true"><circle cx="12" cy="12" r="10" fill="none" stroke="#93874a" stroke-width="3"/></svg>
          <span>@morvanehairstudio</span>
        </li>
        <li>
          <svg class="contact-icon" viewBox="0 0 24 24" aria-hidden="true"><circle cx="12" cy="12" r="11" fill="#93874a"/></svg>
          <span>www.morvanehairstudio-demo.com</span>
        </li>
      </ul>
    </div>
  </section>

  <section class="card card-back">
    <div class="monogram-pattern" role="img" aria-label="Tone-on-tone repeating monogram pattern in black spot gloss"></div>
    <p class="back-name">Morvane Hair Studio</p>
  </section>

</main>
</body>
</html>
```